Real Estate Wordpress Landing Page

I'm looking to a landing page dedicated to my real estate brokerage that's catered to promoting that my company provides 1.5% listings to home sellers... I have a couple examples that I'm really looking towards mocking in a version with similar color schemes using my current company colors/website.

http://halvorik.com/
https://www.brambelo.com/about/one-percent-listing-fee

My brokerage company website is http://www.clearmarrow.us/

Target Market(s)

real estate home sellers & buyers

Industry/Entity Type

Real Estate

Coding

Coded - Design and coding required

Number of Pages Required

1 page

Colors
3176b5
0255a3
eaf1f7
cedeed

Requirements
Must have
• Company website colors - http://www.clearmarrow.us/
• Something around the lines of this website page - http://halvorik.com/
• Wordpress compatibility

```html
<!DOCTYPE html>
<html lang="en">
<head>
<meta charset="utf-8">
<title>Clearmarrow Realty – 1.5% Listing Commission</title>
<link href="https://fonts.googleapis.com/css2?family=Ubuntu:wght@400;500;700&display=swap" rel="stylesheet">
<style>
:root{
  --blue:#3176b5;
  --blue-deep:#0255a3;
  --blue-bright:#2a8ee0;
  --sky:#2b9be0;
  --page:#eef1f6;
  --pale:#eaf1f7;
  --line:#cedeed;
  --ink:#1c2330;
  --muted:#555e6b;
  --green:#3cb43c;
  --violet:#6c63d9;
  --violet-soft:#a9a4ee;
  --white:#ffffff;
  --footer-a:#1a6be6;
  --footer-b:#2a5fe0;
  --footer-bar:#173e9e;
}
*{box-sizing:border-box;margin:0;padding:0}
html,body{width:1200px;height:3000px;overflow:hidden}
body{font-family:"Ubuntu",sans-serif;background:var(--page);color:var(--ink);position:relative}
.abs{position:absolute}

/* top bar & nav */
.topbar{left:0;top:0;width:1200px;height:24px;background:var(--blue-deep);color:var(--white);font-size:10px;display:flex;align-items:center;padding-left:214px;gap:14px}
.topbar b{font-weight:500}
.nav{left:0;top:24px;width:1200px;height:40px;background:var(--white);display:flex;align-items:center;padding-left:186px;font-size:11px;gap:28px;color:var(--ink)}
.nav .active{color:var(--blue);border-bottom:2px solid var(--blue);padding:12px 0 10px}
.nav .caret{font-size:9px;margin-left:4px}
.nav-search{left:1016px;top:30px;width:96px;height:26px;border:1px solid var(--line);border-radius:3px;font-size:10px;color:#9aa3ad;padding:7px 8px}
.nav-go{left:1110px;top:30px;width:32px;height:26px;background:var(--sky);color:var(--white);font-size:10px;border-radius:3px;display:flex;align-items:center;justify-content:center}
.brand{left:60px;top:0;width:112px;height:112px;background:var(--white);box-shadow:0 2px 6px rgba(0,0,0,.2);display:flex;flex-direction:column;align-items:center;justify-content:center;gap:8px;z-index:3}
.brand-square{width:34px;height:34px;background:var(--blue-deep)}
.brand-name{font-size:13px;font-weight:700;color:var(--blue-deep)}

/* hero */
.hero{left:0;top:64px;width:1200px;height:482px;background:linear-gradient(180deg,#2b2a2a 0%,#4a3e33 35%,#2f2d2c 70%,#1b1d22 100%)}
.hero-title{left:0;top:240px;width:1200px;text-align:center;color:var(--white);font-size:24px;font-weight:700}
.hero-sub{left:0;top:276px;width:1200px;text-align:center;color:var(--white);font-size:13px;font-weight:500}
.search-row{left:76px;top:438px;width:1050px;display:flex;gap:20px}
.field{flex:1;height:24px;background:var(--white);border-radius:2px;font-size:9px;color:#8a929c;padding:7px 8px;display:flex;justify-content:space-between}
.search-btn{left:76px;top:470px;width:1048px;height:30px;background:var(--blue-bright);color:var(--white);font-size:10px;display:flex;align-items:center;justify-content:center;border-radius:2px}
.hero-down{left:586px;top:510px;width:28px;height:28px}

/* contact widget */
.widget{left:956px;top:574px;width:224px;height:362px;background:var(--white);box-shadow:0 1px 4px rgba(0,0,0,.15)}
.widget-head{height:32px;background:var(--sky);color:var(--white);font-size:10px;display:flex;align-items:center;padding:0 12px;gap:8px}
.widget-head .chev{margin-left:auto}
.widget-body{padding:14px 10px}
.widget h4{font-size:10px;font-weight:700}
.widget p{font-size:9px;color:var(--muted);margin:4px 0 10px}
.w-input{height:30px;border:1px solid var(--line);margin-bottom:8px;font-size:9px;color:#8a929c;display:flex;align-items:center;gap:12px;padding:0 10px}
.w-area{height:80px;border:1px solid var(--line);font-size:9px;color:#8a929c;padding:8px}
.w-checks{display:grid;grid-template-columns:1fr 1fr;font-size:9px;color:var(--muted);gap:4px;margin:8px 0 12px}
.w-checks span::before{content:"";display:inline-block;width:8px;height:8px;border:1px solid #999;margin-right:5px;vertical-align:-1px}
.w-send{height:30px;background:var(--sky);color:var(--white);font-size:9px;display:flex;align-items:center;justify-content:center}

/* services */
.svc-label{left:252px;width:708px;text-align:center;font-size:9px;color:var(--muted)}
.svc-title{left:252px;width:708px;text-align:center;font-size:10px;font-weight:700}
.rule{left:252px;width:708px;height:1px;background:var(--line)}
.cols{left:252px;width:720px;display:flex;gap:0}
.col{width:180px;padding-right:18px}
.icon{width:40px;height:40px;margin-bottom:14px}
.col h3{font-size:11px;font-weight:700;margin-bottom:6px;line-height:1.3}
.col p{font-size:9px;color:var(--muted);line-height:1.45}
.btn-green{height:30px;background:var(--green);color:var(--white);font-size:9px;font-weight:500;display:flex;align-items:center;justify-content:center}

/* properties map */
.sec-title{left:252px;font-size:11px;font-weight:700}
.tabs{left:252px;top:1562px;display:flex}
.tab{height:36px;padding:0 20px;font-size:9px;display:flex;align-items:center;border:1px solid var(--line);color:var(--muted);background:var(--page)}
.tab.on{background:var(--white);color:var(--ink);font-weight:500;border-bottom-color:var(--white)}
.map{left:252px;top:1612px;width:698px;height:380px;background:linear-gradient(135deg,#eef0f2,#e4e7ea 60%,#dfe3e7);border:1px solid var(--line)}

/* cards */
.cards{left:252px;top:2086px;display:flex;gap:12px}
.card{width:166px;height:234px;background:var(--sky);color:var(--white)}
.card-photo{height:110px;background:linear-gradient(180deg,#f2efe9,#c9c2b6 70%,#8d7f6e)}
.card-photo.warm{background:linear-gradient(180deg,#3c3732,#8a6a4a 60%,#c8ab86)}
.card-photo.kit{background:linear-gradient(180deg,#f4f1ec,#e9e2d8 50%,#5b8bb5)}
.card-body{padding:10px 8px;border-top:10px solid var(--page)}
.card-loc{font-size:8px;margin-bottom:6px}
.card-name{font-size:11px;font-weight:700;line-height:1.3}
.card-id{font-size:8px;margin:6px 0 8px}
.card-price{font-size:12px;font-weight:700}

/* talk box */
.talk{left:280px;top:2414px;width:644px;height:206px;background:var(--white);border:1px solid var(--line);display:flex}
.talk-l{width:300px;padding:30px 22px}
.talk small{font-size:9px;color:var(--muted);display:block;margin-bottom:10px}
.talk h2{font-size:15px;font-weight:500;margin-bottom:10px}
.talk .mail{font-size:9px;color:var(--blue)}
.talk .note{font-size:9px;color:var(--muted);margin-top:6px}
.talk .note span{color:var(--blue)}
.talk-person{width:64px;margin-right:10px;align-self:flex-end;height:170px;background:linear-gradient(180deg,#e9dfd6,#f7f5f3 60%,#d8d6d4);border-radius:30px 30px 0 0}
.talk-r{flex:1;padding:30px 22px;border-left:1px solid var(--line)}
.talk-r .hours{font-size:9px;color:var(--muted)}

/* footer */
.footer{left:0;top:2670px;width:1200px;height:270px;background:linear-gradient(90deg,var(--footer-a),var(--footer-b));color:var(--white)}
.foot-logo{left:248px;top:2702px;width:170px;height:100px;background:var(--white);display:flex;align-items:center;justify-content:center;gap:8px}
.foot-logo span{font-size:14px;font-weight:700;color:var(--blue-deep)}
.foot-logo i{width:18px;height:18px;background:var(--blue-deep)}
.foot-contact{left:248px;top:2824px;font-size:9px;line-height:1.95;color:var(--white)}
.foot-contact h5{font-size:11px;margin-bottom:4px}
.foot-company{left:626px;top:2700px;width:360px;font-size:9px;color:var(--white)}
.foot-company h5{font-size:11px;margin-bottom:10px}
.foot-links{display:flex;gap:30px;margin-left:14px;margin-bottom:18px;white-space:nowrap}
.foot-company p{line-height:1.5;width:330px}
.socials{display:flex;gap:28px;margin:14px 0 0 14px}
.socials i{width:9px;height:9px;border-radius:50%;background:rgba(255,255,255,.7)}
.bottombar{left:0;top:2940px;width:1200px;height:60px;background:var(--footer-bar);color:var(--white);font-size:9px}
.bottombar span{position:absolute;top:20px}
</style>
</head>
<body>

<div class="abs topbar"><span>Book Your Visit Today, Call: <b>555-310-4821</b></span><span>|</span><b>contact@clearmarrow.us</b></div>
<nav class="abs nav">
  <span class="active">Home</span>
  <span>Services<span class="caret">›</span></span>
  <span>Rentals<span class="caret">›</span></span>
  <span>Video Blog</span>
  <span>About us<span class="caret">›</span></span>
  <span>Contact</span>
</nav>
<div class="abs nav-search">Search...</div>
<div class="abs nav-go">Go</div>
<div class="abs brand"><i class="brand-square"></i><span class="brand-name">Clearmarrow</span></div>

<section class="abs hero" role="img" aria-label="Dusk view from a rooftop terrace with lounge furniture over city buildings"></section>
<h1 class="abs hero-title">Get Full Service for a 1.5% Listing Commission</h1>
<p class="abs hero-sub">See how selling with a Clearmarrow Agent can get you better results for a lower commission.*</p>
<div class="abs search-row">
  <div class="field">Enter City or Zip</div>
  <div class="field">House/Condo<span>▾</span></div>
  <div class="field">Min. Price</div>
  <div class="field">Max. Price</div>
  <div class="field">Any<span>▾</span></div>
  <div class="field">Any<span>▾</span></div>
</div>
<div class="abs search-btn">Search</div>
<svg class="abs hero-down" viewBox="0 0 28 28"><circle cx="14" cy="14" r="12.5" fill="none" stroke="#fff" stroke-width="1.5"/><path d="M9 12l5 5 5-5" fill="none" stroke="#fff" stroke-width="1.6"/></svg>

<aside class="abs widget">
  <div class="widget-head">
    <svg width="12" height="10" viewBox="0 0 12 10"><rect x=".5" y=".5" width="8" height="6" rx="1" fill="none" stroke="#fff"/><rect x="3.5" y="3.5" width="8" height="6" rx="1" fill="none" stroke="#fff"/></svg>
    Contact Us<span class="chev">⌄</span>
  </div>
  <div class="widget-body">
    <h4>How Can We Help You?</h4>
    <p>Please, leave us your message.</p>
    <div class="w-input"><svg width="10" height="10" viewBox="0 0 10 10"><circle cx="5" cy="3" r="2.4" fill="#333"/><path d="M0 10a5 4 0 0 1 10 0z" fill="#333"/></svg>Enter your name</div>
    <div class="w-input"><svg width="11" height="8" viewBox="0 0 11 8"><rect x=".5" y=".5" width="10" height="7" fill="none" stroke="#333"/><path d="M.5.5l5 4 5-4" fill="none" stroke="#333"/></svg>Enter your email</div>
    <div class="w-input"><svg width="10" height="10" viewBox="0 0 10 10"><path d="M2 0l2 2.5-1 1.5c.8 1.5 1.5 2.2 3 3l1.5-1 2.5 2-1.5 2C3.5 9.5.5 6.5 0 1.5z" fill="none" stroke="#333"/></svg>Enter your phone</div>
    <div class="w-area">Your Message</div>
    <div class="w-checks"><span>I'm a Owner</span><span>I'm a Renter</span><span>I'm a Contractor</span><span>Other</span></div>
    <div class="w-send">Send Message</div>
  </div>
</aside>

<!-- homeowners -->
<div class="abs svc-label" style="top:656px">Services</div>
<div class="abs svc-title" style="top:676px">For Homeowners</div>
<div class="abs rule" style="top:710px"></div>
<div class="abs cols" style="top:766px">
  <div class="col"><svg class="icon" role="img" aria-label="Marketing icon" viewBox="0 0 40 40"><rect x="4" y="8" width="32" height="26" rx="3" fill="var(--violet-soft)"/><rect x="10" y="20" width="4" height="10" fill="var(--violet)"/><rect x="18" y="14" width="4" height="16" fill="var(--violet)"/><rect x="26" y="18" width="4" height="12" fill="var(--violet)"/></svg><h3>Market Your Rental</h3><p>Get maximum exposure across 40+ sites and listing platforms, including our network of local companies and relocation agents.</p></div>
  <div class="col"><svg class="icon" role="img" aria-label="Calendar icon" viewBox="0 0 40 40"><rect x="4" y="8" width="30" height="26" rx="3" fill="var(--violet-soft)"/><rect x="4" y="8" width="30" height="7" fill="var(--violet)"/><circle cx="30" cy="30" r="7" fill="var(--violet)"/></svg><h3>On-demand Showings</h3><p>Our professional FieldHosts conduct on-demand showings to prospects any day of the week.</p></div>
  <div class="col"><svg class="icon" role="img" aria-label="Renter check icon" viewBox="0 0 40 40"><circle cx="16" cy="13" r="7" fill="var(--violet)"/><path d="M3 36a13 11 0 0 1 26 0z" fill="var(--violet-soft)"/><circle cx="30" cy="28" r="7" fill="var(--violet)"/><path d="M27 28l2 2 4-4" stroke="#fff" stroke-width="1.6" fill="none"/></svg><h3>Get High-quality Renters</h3><p>Select only from qualified renters vetted by our quick yet thorough screening process.</p></div>
  <div class="col"><svg class="icon" role="img" aria-label="Maintenance tools icon" viewBox="0 0 40 40"><rect x="4" y="8" width="24" height="26" rx="2" fill="var(--violet-soft)"/><path d="M12 32L34 8" stroke="var(--violet)" stroke-width="4"/><circle cx="33" cy="9" r="4" fill="var(--violet)"/></svg><h3>24/7 Maintenance Support</h3><p>Never worry about maintenance requests with our Support Team and network of professional vendors.</p></div>
</div>
<div class="abs btn-green" style="left:542px;top:976px;width:120px">Get A Free Rent Estimate</div>

<!-- renters -->
<div class="abs svc-label" style="top:1090px">Services</div>
<div class="abs svc-title" style="top:1110px">For Renters</div>
<div class="abs rule" style="top:1142px"></div>
<div class="abs cols" style="top:1200px">
  <div class="col"><svg class="icon" role="img" aria-label="Listings icon" viewBox="0 0 40 40"><rect x="4" y="6" width="30" height="28" rx="3" fill="var(--violet-soft)"/><rect x="9" y="12" width="20" height="3" fill="var(--violet)"/><rect x="9" y="19" width="20" height="3" fill="var(--violet)"/><rect x="9" y="26" width="14" height="3" fill="var(--violet)"/></svg><h3>View Listings &amp; Book Showings</h3><p>View our listing of quality rentals online then schedule a visit at a day and time convenient to you.</p></div>
  <div class="col"><svg class="icon" role="img" aria-label="Application card icon" viewBox="0 0 40 40"><rect x="3" y="9" width="34" height="24" rx="3" fill="var(--violet-soft)"/><circle cx="13" cy="21" r="5" fill="var(--violet)"/><rect x="21" y="17" width="11" height="3" fill="var(--violet)"/><rect x="21" y="23" width="8" height="3" fill="var(--violet)"/></svg><h3>Apply &amp; Qualify for Free</h3><p>Submit a free and secure digital application and qualify within 24 hours. Use one app for all listings.</p></div>
  <div class="col"><svg class="icon" role="img" aria-label="Moving box icon" viewBox="0 0 40 40"><path d="M20 4l15 8v16l-15 8-15-8V12z" fill="var(--violet-soft)"/><path d="M5 12l15 8 15-8M20 20v16" fill="none" stroke="var(--violet)" stroke-width="2"/></svg><h3>Move-in Easily</h3><p>Your new rental home is inspected and cleaned so you can move-in smoothly and easily.</p></div>
  <div class="col"><svg class="icon" role="img" aria-label="Maintenance tools icon" viewBox="0 0 40 40"><rect x="4" y="8" width="24" height="26" rx="2" fill="var(--violet-soft)"/><path d="M12 32L34 8" stroke="var(--violet)" stroke-width="4"/><circle cx="33" cy="9" r="4" fill="var(--violet)"/></svg><h3>24/7 Maintenance Support</h3><p>Report issues and monitor maintenance requests any time with our round-the-clock support.</p></div>
</div>
<div class="abs btn-green" style="left:542px;top:1396px;width:114px">Browse Rental Listings</div>

<!-- managed properties -->
<div class="abs sec-title" style="top:1512px">Properties Managed By Northvale</div>
<div class="abs rule" style="top:1540px;width:710px"></div>
<div class="abs tabs"><div class="tab on">All Properties</div><div class="tab">Available Properties</div></div>
<div class="abs map" role="img" aria-label="Street map of the neighbourhood showing managed property locations"></div>

<!-- latest -->
<div class="abs sec-title" style="top:2030px">Latest Properties</div>
<div class="abs rule" style="top:2060px;width:710px"></div>
<div class="abs cards">
  <article class="card"><div class="card-photo" role="img" aria-label="Bright dining room with large windows"></div><div class="card-body"><div class="card-loc">Harlow Cove | Florida</div><div class="card-name">Beautiful home located in downtown, Florida</div><div class="card-id">House@Lot2794</div><div class="card-price">$500,000</div></div></article>
  <article class="card"><div class="card-photo warm" role="img" aria-label="Open living space with glass walls at night"></div><div class="card-body"><div class="card-loc">Harlow Cove | Florida</div><div class="card-name">Beautiful home located in downtown, Florida</div><div class="card-id">House@Lot2794</div><div class="card-price">$500,000</div></div></article>
  <article class="card"><div class="card-photo kit" role="img" aria-label="White kitchen with blue cabinets"></div><div class="card-body"><div class="card-loc">Harlow Cove | Florida</div><div class="card-name">Beautiful home located in downtown, Florida</div><div class="card-id">House@Lot2794</div><div class="card-price">$500,000</div></div></article>
  <article class="card"><div class="card-photo" role="img" aria-label="Bright dining room with large windows"></div><div class="card-body"><div class="card-loc">Harlow Cove | Florida</div><div class="card-name">Beautiful home located in downtown, Florida</div><div class="card-id">House@Lot2794</div><div class="card-price">$500,000</div></div></article>
</div>
<div class="abs rule" style="top:2360px;width:710px"></div>

<!-- talk -->
<section class="abs talk">
  <div class="talk-l">
    <small>Contact Us</small>
    <h2>Are You Ready? Let's Talk</h2>
    <div class="mail">contact@clearmarrow.us</div>
    <div class="note">Or contact us using our <span>Live Chat!</span></div>
  </div>
  <div class="talk-person" role="img" aria-label="Support agent with headset"></div>
  <div class="talk-r">
    <small>Call Us</small>
    <h2>Get In Touch With Us</h2>
    <div class="mail">555-310-7702</div>
    <div class="hours">9:00 am to 5:00 pm</div>
  </div>
</section>

<!-- footer -->
<footer class="abs footer"></footer>
<div class="abs foot-logo"><i></i><span>Clearmarrow</span></div>
<div class="abs foot-contact">
  <h5>Contact Us</h5>
  240 Larkspur Ave, Ste 12, Harlow Cove, FL 30918<br>555-310-7702<br>555-310-0919<br>contact@clearmarrow.us
</div>
<div class="abs foot-company">
  <h5>Company</h5>
  <div class="foot-links"><span>Services</span><span>Rentals</span><span>Video Blog</span><span>About Us</span><span>Contact</span></div>
  <p>The Clearmarrow Realty team is dedicated to keeping you up to date with the real estate market.Don't forget to follow us on</p>
  <div class="socials"><i></i><i></i><i></i><i></i><i></i><i></i></div>
</div>
<div class="abs bottombar">
  <span style="left:66px">Clearmarrow.us - All rights reserved.</span>
  <span style="left:488px">Privacy</span>
  <span style="left:640px">Terms and Conditions</span>
  <span style="left:848px">Contact Us</span>
  <span style="left:1014px">Mobile Notary</span>
</div>

</body>
</html>
```